Company or website name
- www.tovirka.me
- Describe your company and organization and target audience
- Our small factory makes organic chocolate with honey instead of sugar and creates jobs for people with special needs in Pereslavl-Zalessky / Russia.
- The design should have the following
- At the moment we are searching for a designer to create some labels for new tastes of chocolate in the same style we already use. Here are some examples of our packagings: http://tovirka.me/product-category/assortment/ What we need are illustrations of new tastes in the center of the packaging. The rest of the packaging should remain unchanged. The new tastes are: - Dark chocolate with Goji berries and crushed cocoa beans - Dark chocolate with Cashew nuts and basil - Dark chocolate with Hibisсus - Dark chocolate with Barberry - Milk chocolate We can pay 100 $ for the five labels (20 $ for each). We know, it's not a lot, but we hope to find the right

```html
<!DOCTYPE html>
<html lang="ru">
<head>
<meta charset="utf-8">
<title>Шоколад на меду — этикетки</title>
<link href="https://fonts.googleapis.com/css2?family=Oswald:wght@600&family=Marck+Script&family=PT+Serif&family=Roboto+Condensed:wght@400;700&display=swap" rel="stylesheet">
<style>
  :root {
    --backdrop: #e4e3e0;
    --kraft: #c8a674;
    --kraft-light: #d3b585;
    --ink: #2f2923;
    --ink-soft: #4a3f33;
    --crimp: #55524d;
    --art: #3a3028;
    --comb: #b8956a;
  }
  * { box-sizing: border-box; margin: 0; padding: 0; }
  html, body { width: 1200px; height: 565px; overflow: hidden; }
  body {
    background: var(--backdrop);
    position: relative;
    font-family: "Roboto Condensed", sans-serif;
    color: var(--ink);
  }
  .bar {
    position: absolute;
    top: 198px;
    width: 142px;
    height: 282px;
    background: radial-gradient(ellipse at 50% 40%, var(--kraft-light), var(--kraft));
    box-shadow: 0 2px 6px rgba(0,0,0,.18);
    text-align: center;
  }
  .bar::before, .bar::after {
    content: "";
    position: absolute;
    left: 0; right: 0;
    height: 6px;
    background: var(--crimp);
  }
  .bar::before { top: 0; opacity: .55; height: 4px; }
  .bar::after { bottom: 0; }
  .maker {
    position: absolute;
    top: 14px; left: 0; right: 0;
    font-family: "PT Serif", serif;
    font-size: 8px;
    line-height: 1.2;
    color: var(--ink-soft);
  }
  .maker-mark {
    display: block;
    width: 22px; height: 22px;
    margin: 0 auto 5px;
    border-radius: 50%;
    border: 1.5px solid var(--ink-soft);
  }
  .title {
    position: absolute;
    top: 72px; left: 0; right: 0;
    font-family: "Oswald", sans-serif;
    font-weight: 600;
    font-size: 27px;
    letter-spacing: 1px;
    line-height: 1;
  }
  .subtitle {
    position: absolute;
    top: 103px; left: 14px; right: 14px;
    display: flex; align-items: center; gap: 6px;
    font-family: "Marck Script", cursive;
    font-size: 16px;
  }
  .subtitle::before, .subtitle::after {
    content: ""; flex: 1; height: 1px; background: var(--ink);
  }
  .stamp {
    position: absolute;
    top: 108px; right: 8px;
    width: 34px;
    padding: 2px 1px;
    border: 1px solid var(--ink);
    outline: 1px dashed var(--ink);
    outline-offset: 1px;
    transform: rotate(-18deg);
    font-size: 5px;
    line-height: 1.1;
    font-weight: 700;
    text-transform: uppercase;
  }
  .flavour-art {
    position: absolute;
    top: 130px; left: 33px;
    width: 76px; height: 70px;
    border-radius: 8px;
    background: radial-gradient(circle at 50% 50%, var(--art) 0 38%, var(--comb) 40% 60%, transparent 72%);
  }
  .strength {
    position: absolute;
    top: 207px; left: 8px; right: 8px;
    height: 13px;
    background: var(--ink);
    color: var(--kraft-light);
    font-size: 8px;
    font-weight: 700;
    line-height: 13px;
    letter-spacing: .3px;
    clip-path: polygon(0 0, 100% 0, 94% 50%, 100% 100%, 0 100%, 6% 50%);
  }
  .recipe {
    position: absolute;
    top: 231px; left: 0; right: 0;
    font-size: 6px;
    text-transform: uppercase;
    color: var(--ink-soft);
  }
  .weight {
    position: absolute;
    top: 249px; left: 0; right: 0;
    font-size: 9px;
    font-weight: 700;
  }
</style>
</head>
<body>

<div class="bar" style="left:63px">
  <div class="maker"><span class="maker-mark"></span>Шоколадная мастерская<br>в Лесной Слободе</div>
  <div class="title">ШОКОЛАД</div>
  <div class="subtitle">на меду</div>
  <div class="flavour-art" role="img" aria-label="Illustration of barberry twig on honeycomb"></div>
  <div class="strength">ГОРЬКИЙ | 70% КАКАО</div>
  <div class="recipe">Состав: какао тертое, мед, какао масло</div>
  <div class="weight">90 ГР</div>
</div>

<div class="bar" style="left:294px">
  <div class="maker"><span class="maker-mark"></span>Шоколадная мастерская<br>в Лесной Слободе</div>
  <div class="title">ШОКОЛАД</div>
  <div class="subtitle">на меду</div>
  <div class="stamp">мёд вместо сахара</div>
  <div class="flavour-art" role="img" aria-label="Illustration of hibiscus flower on honeycomb"></div>
  <div class="strength">ГОРЬКИЙ | 70% КАКАО</div>
  <div class="recipe">Состав: какао тертое, мед, какао масло</div>
  <div class="weight">90 ГР</div>
</div>

<div class="bar" style="left:525px">
  <div class="maker"><span class="maker-mark"></span>Шоколадная мастерская<br>в Лесной Слободе</div>
  <div class="title">ШОКОЛАД</div>
  <div class="subtitle">на меду</div>
  <div class="stamp">мёд вместо сахара</div>
  <div class="flavour-art" role="img" aria-label="Illustration of cashew nuts and basil leaves on honeycomb"></div>
  <div class="strength">ГОРЬКИЙ | 70% КАКАО</div>
  <div class="recipe">Состав: какао тертое, мед, какао масло</div>
  <div class="weight">90 ГР</div>
</div>

<div class="bar" style="left:757px">
  <div class="maker"><span class="maker-mark"></span>Шоколадная мастерская<br>в Лесной Слободе</div>
  <div class="title">ШОКОЛАД</div>
  <div class="subtitle">на меду</div>
  <div class="stamp">мёд вместо сахара</div>
  <div class="flavour-art" role="img" aria-label="Illustration of goji berries and a cocoa pod on honeycomb"></div>
  <div class="strength">ГОРЬКИЙ | 70% КАКАО</div>
  <div class="recipe">Состав: какао тертое, мед, какао масло</div>
  <div class="weight">90 ГР</div>
</div>

<div class="bar" style="left:990px">
  <div class="maker"><span class="maker-mark"></span>Шоколадная мастерская<br>в Лесной Слободе</div>
  <div class="title">ШОКОЛАД</div>
  <div class="subtitle">на меду</div>
  <div class="stamp">мёд вместо сахара</div>
  <div class="flavour-art" role="img" aria-label="Illustration of a milk bottle pouring on honeycomb"></div>
  <div class="strength">ГОРЬКИЙ | 70% КАКАО</div>
  <div class="recipe">Состав: какао тертое, мед, какао масло</div>
  <div class="weight">90 ГР</div>
</div>

</body>
</html>
```